Steadfast MD - Sleep Medicine Specialist - Business Cards

We are a new medical practice called Steadfast MD. We are sleep medicine specialists and we will be conducting sleep studies on patients with sleep related ailments. We want the business card to be bold, professional, and clean with the logo as the stand out visual piece. We dont like wild flashy designs. We want our design to be bold and classic while at the same time conveying who we are and what we do. We are reliable, professional, and the best in the business.

Industry/Entity Type

Health Care

Contact Information for Business Card

- Clean
- Bold
- Classic
- not cluttered

Requirements
Must have
• logo, website, phone number
Nice to have
• several options to choose from
Should not have
• flashy imaged - reflective print - images of people sleeping

```html
<!DOCTYPE html>
<html lang="en">
<head>
<meta charset="utf-8">
<title>Steadfast MD – Business Card</title>
<link rel="stylesheet" href="https://fonts.googleapis.com/css2?family=Poppins:wght@400;500;700;800&display=swap">
<style>
  :root {
    --backdrop: #2a2a2a;
    --brand-red: #e60000;
    --accent-red: #e41f26;
    --ink: #111111;
    --paper: #ffffff;
    --social: #4a6fb5;
  }
  * { box-sizing: border-box; margin: 0; padding: 0; }
  html, body {
    width: 1200px; height: 1189px; overflow: hidden;
    background: var(--backdrop);
    font-family: "Poppins", sans-serif;
  }
  .sheet {
    position: relative; width: 1200px; height: 1189px;
    display: flex; flex-direction: column; align-items: center; justify-content: center; gap: 56px;
  }
  .card {
    position: relative; width: 900px; height: 514px; border-radius: 28px; overflow: hidden;
    box-shadow: 0 14px 30px rgba(0,0,0,.45);
  }
  /* Front */
  .card-front { background: var(--brand-red); display: flex; align-items: center; justify-content: center; gap: 22px; }
  .front-mark {
    width: 96px; height: 96px; border-radius: 50%;
    border: 6px solid var(--paper); flex: none;
  }
  .front-name { color: var(--paper); font-weight: 800; font-size: 64px; letter-spacing: -1px; }

  /* Back */
  .card-back { background: var(--paper); }
  .back-info { position: absolute; left: 64px; top: 70px; }
  .wordmark { color: var(--ink); font-weight: 800; font-size: 56px; line-height: 1; letter-spacing: -1.5px; }
  .person { margin-top: 34px; font-weight: 700; font-size: 28px; color: var(--ink); line-height: 1.1; }
  .role { font-weight: 400; font-size: 21px; color: var(--accent-red); margin-top: 4px; }
  .contacts, .socials { list-style: none; margin-top: 28px; }
  .socials { margin-top: 18px; }
  .contacts li, .socials li {
    display: flex; align-items: center; gap: 14px;
    font-size: 23px; font-weight: 500; color: var(--ink); line-height: 1.45;
  }
  .icon { width: 26px; height: 26px; flex: none; }
  .dot { width: 24px; height: 24px; border-radius: 50%; background: var(--social); flex: none; }
  .back-mark {
    position: absolute; right: 60px; top: 107px; width: 300px; height: 300px;
    display: flex; flex-direction: column; align-items: center; justify-content: center; gap: 18px;
  }
  .back-mark-circle { width: 110px; height: 110px; border-radius: 50%; border: 10px solid var(--accent-red); }
  .back-mark-name { color: var(--accent-red); font-weight: 800; font-size: 40px; letter-spacing: -1px; }
</style>
</head>
<body>
<main class="sheet">
  <section class="card card-front" aria-label="Card front">
    <span class="front-mark" aria-hidden="true"></span>
    <span class="front-name">SteadfastMD.com</span>
  </section>

  <section class="card card-back" aria-label="Card back">
    <div class="back-info">
      <div class="wordmark">SteadfastMD.com</div>
      <p class="person">Dr. Dana Whitlock, MD</p>
      <p class="role">Board Certified Sleep Medicine, CMO</p>
      <ul class="contacts">
        <li>
          <svg class="icon" viewBox="0 0 26 26" aria-hidden="true">
            <circle cx="13" cy="13" r="13" fill="var(--accent-red)"/>
            <path d="M8 7.5c1-.8 2-.6 2.6.3l1 1.6c.4.7.2 1.4-.4 1.8l-.7.5c.6 1.5 1.9 2.9 3.4 3.6l.5-.7c.4-.6 1.2-.8 1.8-.4l1.6 1c.9.6 1.1 1.7.3 2.6-1.2 1.3-3 1.5-4.7.5-2.6-1.5-4.6-3.7-5.8-6.3-.8-1.7-.6-3.4.4-4.5z" fill="#fff"/>
          </svg>
          555-014-2298
        </li>
        <li>
          <svg class="icon" viewBox="0 0 26 26" aria-hidden="true">
            <circle cx="13" cy="13" r="13" fill="var(--accent-red)"/>
            <rect x="6.5" y="8.5" width="13" height="9" rx="1" fill="none" stroke="#fff" stroke-width="1.6"/>
            <path d="M6.8 9l6.2 5 6.2-5" fill="none" stroke="#fff" stroke-width="1.6"/>
          </svg>
          drwhitlock@steadfastmd.com
        </li>
      </ul>
      <ul class="socials">
        <li><span class="dot" aria-hidden="true"></span>SteadfastMd</li>
        <li><span class="dot" aria-hidden="true"></span>steadfast_md</li>
        <li><span class="dot" aria-hidden="true"></span>Steadfastmd</li>
      </ul>
    </div>
    <div class="back-mark">
      <span class="back-mark-circle" aria-hidden="true"></span>
      <span class="back-mark-name">Steadfast MD</span>
    </div>
  </section>
</main>
</body>
</html>
```